Sticker to put on shipping boxes-Pet ProductDelivery

I am looking for a sticker to put on the exterior of brown shipping boxes. We deliver pet products to a local consumer base and if our clients are not home, we leave the products on the door step. We would like to place a sticker on the box so that when looking at the box the consumer knows it came from us.

Looking for a design that is not larger than about a 3x5 or 5x5? I want it large enough to stand out, yet not so large that it is overwhelming. It also does not have to be square. It can also be rectangle. It will be placed in a bottom corner.

The design need to stand out on a brown box.

Attached is our logo for you to play around with.

Take note that the file with our slogan has colors mixes up.

The words 'Premium Pet Products' should be the same gray and the word 'Pet'. And the word 'Delivered' the same color as the word 'Brisk'.

Target Market(s)

Audience is mid 20's to seniors in senior living complexes. Those interested in convince and too buy to shop for themselves.

Industry/Entity Type

Shipping

Requirements
Must have
• Color but not overwhelming.

Orange, green, blue to match the logo colors.
Should not have
• Does not need to have a lot of text. Focus more on the Brisk Hound name and logo.

```html
<!DOCTYPE html>
<html lang="en">
<head>
<meta charset="utf-8">
<title>Brisk Hound – Shipping Sticker</title>
<link href="https://fonts.googleapis.com/css2?family=Ubuntu:ital,wght@0,400;1,700&display=swap" rel="stylesheet">
<style>
  :root {
    --backdrop: #e9e4de;
    --sticker-white: #ffffff;
    --brand-gray: #6d6e71;
    --brand-green: #9dc63b;
    --slogan-white: #ffffff;
  }
  * { margin: 0; padding: 0; box-sizing: border-box; }
  html, body {
    width: 1200px;
    height: 1000px;
    overflow: hidden;
    background: var(--backdrop);
  }
  .canvas {
    width: 1200px;
    height: 1000px;
    display: flex;
    align-items: center;
    justify-content: center;
  }
  .sticker {
    width: 500px;
    height: 600px;
    background: var(--sticker-white);
    border-radius: 36px;
    overflow: hidden;
    display: flex;
    flex-direction: column;
    box-shadow: 0 6px 24px rgba(0, 0, 0, 0.12);
  }
  .sticker__brand {
    flex: 1;
    display: flex;
    align-items: center;
    justify-content: center;
    gap: 16px;
    padding: 0 40px;
  }
  .brand-dot {
    flex: none;
    width: 28px;
    height: 28px;
    border-radius: 50%;
    background: var(--brand-green);
  }
  .brand-name {
    font-family: "Ubuntu", sans-serif;
    font-weight: 400;
    font-size: 62px;
    line-height: 1;
    letter-spacing: -1px;
    white-space: nowrap;
    color: var(--brand-gray);
  }
  .sticker__band {
    flex: none;
    height: 150px;
    background: var(--brand-green);
    display: flex;
    align-items: center;
    justify-content: center;
    padding: 0 24px;
  }
  .slogan {
    font-family: "Ubuntu", sans-serif;
    font-style: italic;
    font-weight: 700;
    font-size: 19px;
    letter-spacing: 0.2px;
    white-space: nowrap;
    text-transform: uppercase;
    color: var(--slogan-white);
  }
</style>
</head>
<body>
  <main class="canvas">
    <section class="sticker">
      <div class="sticker__brand">
        <span class="brand-dot" aria-hidden="true"></span>
        <span class="brand-name">Brisk Hound</span>
      </div>
      <div class="sticker__band">
        <p class="slogan">Premium Pet Products Delivered</p>
      </div>
    </section>
  </main>
</body>
</html>
```